Pediatric Pelvic Health Brochure

Looking to design a brochure for Marlow Brook's pelvic health program. I can provide imagery once I see the layout. Our website is marlowbrookpt.example so the look should reflect that

If you see PDF titled blue and word doc you will see what we provided as thoguhts.

Target Market(s)

parents of children

Industry/Entity Type

Health And Wellness

Font styles to use
Serif

Requirements
Must have
• clear call outs - easy to read with copy,
Should not have
• not look bland or dated

```html
<!DOCTYPE html>
<html lang="en">
<head>
<meta charset="utf-8">
<title>Pediatric Pelvic Health Brochure</title>
<link href="https://fonts.googleapis.com/css2?family=Libre+Baskerville:wght@400;700&family=Montserrat:wght@600;700;800&family=Open+Sans:wght@400;600&display=swap" rel="stylesheet">
<style>
  :root{
    --navy:#1d3585;
    --navy-deep:#14296e;
    --cyan:#1aa7e0;
    --paper:#f4f6f9;
    --mist:#e6ebf2;
    --ink:#2a3550;
    --stage:#d9dbde;
    --white:#ffffff;
  }
  *{box-sizing:border-box;margin:0;padding:0}
  html,body{width:1200px;height:2400px;overflow:hidden;background:var(--stage)}
  body{position:relative;font-family:"Open Sans",Arial,sans-serif;color:var(--ink)}
  .spread{position:absolute;left:45px;width:1110px;height:860px;display:flex;box-shadow:0 10px 30px rgba(0,0,0,.18)}
  .spread-outside{top:200px}
  .spread-inside{top:1240px}
  .panel{position:relative;width:370px;height:860px;overflow:hidden}
  .panel + .panel{border-left:1px solid rgba(0,0,0,.06)}
  .panel-light{background:var(--paper)}
  .panel-blue{background:linear-gradient(180deg,var(--navy) 0%,var(--navy-deep) 100%);color:var(--white)}
  .photo{position:absolute;left:0;right:0}
  .curve{position:absolute;left:0;width:370px}
  .serif-head{font-family:"Libre Baskerville",Georgia,serif;text-transform:uppercase;letter-spacing:.5px}
  .title{font-family:"Montserrat",Arial,sans-serif;font-weight:800;text-transform:uppercase;line-height:1.1;letter-spacing:1px}
  .subtitle{font-family:"Libre Baskerville",Georgia,serif;color:var(--cyan);text-transform:uppercase;font-size:14px;letter-spacing:.5px;line-height:1.3}
  .url-pill{position:absolute;left:30px;right:30px;height:34px;border-radius:17px;background:var(--white);color:var(--navy);display:flex;align-items:center;justify-content:center;gap:8px;font-family:"Montserrat",Arial,sans-serif;font-weight:700;font-size:14px}
  .url-bar{position:absolute;left:0;right:0;bottom:0;height:40px;background:var(--cyan);color:var(--white);display:flex;align-items:center;justify-content:center;gap:8px;font-family:"Montserrat",Arial,sans-serif;font-weight:700;font-size:14px}
  .copy{font-size:12.5px;line-height:1.6}
  .copy p + p{margin-top:12px}

  /* brand name on the cover */
  .brand{position:absolute;top:0;left:0;right:0;height:105px;display:flex;align-items:center;justify-content:center}
  .brand-name{font-family:"Montserrat",Arial,sans-serif;font-weight:700;font-size:24px;letter-spacing:2px;text-transform:uppercase;color:var(--cyan)}

  /* inner flap */
  .diagnoses{position:absolute;top:330px;left:34px;right:28px}
  .diagnoses h3{color:var(--navy);font-size:17px;line-height:1.3;margin-bottom:16px}
  .diagnoses li{list-style:none;position:relative;padding-left:20px;font-size:12.5px;line-height:1.45;margin-bottom:9px}
  .diagnoses li::before{content:"";position:absolute;left:0;top:5px;width:9px;height:9px;border-radius:50%;background:var(--cyan)}

  /* back panel */
  .portrait{position:absolute;top:40px;left:125px;width:120px;height:120px;border-radius:50%;border:5px solid var(--white);background:radial-gradient(circle at 40% 40%,#f3f5f8,#b9c9dc)}
  .back-title{position:absolute;top:190px;left:0;right:0;text-align:center}
  .back-title .title{font-size:30px}
  .back-title .subtitle{margin-top:8px}
  .contact{position:absolute;top:340px;left:30px;right:30px;text-align:center}
  .contact h3{font-family:"Montserrat",Arial,sans-serif;font-weight:800;font-size:24px;margin-bottom:14px}
  .contact .lead{font-size:14px;line-height:1.5}
  .contact-line{margin-top:26px;font-size:14px;line-height:1.5}
  .contact-line svg{display:block;margin:0 auto 6px}

  /* cover */
  .cover-title{position:absolute;top:640px;left:0;right:0;text-align:center;color:var(--white)}
  .cover-title .title{font-size:31px}
  .cover-title .subtitle{margin-top:8px}

  /* inside */
  .section-head{font-size:20px;margin-bottom:18px}
  .help-copy{position:absolute;top:40px;left:34px;right:30px}
  .special-top{position:absolute;top:36px;left:34px;right:30px}
  .special-top .section-head{color:var(--navy);text-align:center}
  .special-bottom{position:absolute;top:560px;left:34px;right:30px}
  .cta-pill{position:absolute;left:30px;right:30px;bottom:26px;height:36px;border-radius:18px;background:var(--cyan);color:var(--white);display:flex;align-items:center;justify-content:center;font-family:"Montserrat",Arial,sans-serif;font-weight:700;font-size:13px}
  .partner-copy{position:absolute;top:330px;left:34px;right:30px}
  .partner-note{margin-top:22px;border:1px solid rgba(255,255,255,.5);padding:14px;font-size:11.5px;line-height:1.5}
</style>
</head>
<body>

<section class="spread spread-outside">

  <article class="panel panel-light panel-flap">
    <div class="photo" style="top:0;height:250px;background:linear-gradient(135deg,#f1e7df,#dcc8bd 55%,#c9d6e6)" role="img" aria-label="Photo of a doctor talking with a smiling young girl"></div>
    <svg class="curve" style="top:205px" height="70" viewBox="0 0 370 70" aria-hidden="true">
      <path d="M0 40 Q185 0 370 30 L370 70 L0 70 Z" fill="var(--paper)"/>
      <path d="M0 40 Q185 0 370 30" fill="none" stroke="var(--cyan)" stroke-width="4"/>
    </svg>
    <div class="diagnoses">
      <h3 class="serif-head">We treat a range<br>of diagnoses</h3>
      <ul>
        <li>Constipation</li>
        <li>Increased urinary frequency</li>
        <li>Decreased urinary frequency</li>
        <li>Day time incontinence</li>
        <li>Night time incontinence, bed-wetting</li>
        <li>Fecal incontinence</li>
        <li>Dysfunctional voiding</li>
        <li>Pain in the abdomen or pelvis</li>
        <li>Post-surgical pelvic recovery</li>
        <li>Treatment after pediatric pelvic surgery</li>
      </ul>
    </div>
    <div class="url-pill" style="bottom:26px;background:var(--navy);color:var(--white)">
      <svg width="16" height="16" viewBox="0 0 16 16" aria-hidden="true"><circle cx="8" cy="8" r="7" fill="none" stroke="currentColor" stroke-width="1.5"/><path d="M1 8h14M8 1c-3 4-3 10 0 14M8 1c3 4 3 10 0 14" fill="none" stroke="currentColor" stroke-width="1.2"/></svg>
      www.marlowbrookpt.example
    </div>
  </article>

  <article class="panel panel-blue panel-back">
    <div class="portrait" role="img" aria-label="Round photo of a doctor with a child holding a teddy bear"></div>
    <div class="back-title">
      <h2 class="title">Pediatric<br>Pelvic Health</h2>
      <p class="subtitle">Treating infants, children<br>&amp; adolescents</p>
    </div>
    <div class="contact">
      <h3>CONTACT US</h3>
      <p class="lead">We offer a FREE 15 minute consultation to help you determine if physical therapy is right for you.</p>
      <p class="contact-line">
        <svg width="22" height="22" viewBox="0 0 24 24" aria-hidden="true"><path d="M6.6 10.8a15 15 0 0 0 6.6 6.6l2.2-2.2a1 1 0 0 1 1-.25 11.4 11.4 0 0 0 3.6.6 1 1 0 0 1 1 1V20a1 1 0 0 1-1 1A17 17 0 0 1 3 4a1 1 0 0 1 1-1h3.5a1 1 0 0 1 1 1c0 1.25.2 2.45.6 3.6a1 1 0 0 1-.25 1z" fill="var(--cyan)"/></svg>
        555.014.2200
      </p>
      <p class="contact-line">
        <svg width="20" height="24" viewBox="0 0 20 24" aria-hidden="true"><path d="M10 0a8 8 0 0 0-8 8c0 6 8 16 8 16s8-10 8-16a8 8 0 0 0-8-8zm0 11a3 3 0 1 1 0-6 3 3 0 0 1 0 6z" fill="var(--cyan)"/></svg>
        120 Harbor Lane<br>Ground Floor<br>Springfield, ST 00000
      </p>
    </div>
    <div class="url-bar">
      <svg width="16" height="16" viewBox="0 0 16 16" aria-hidden="true"><circle cx="8" cy="8" r="7" fill="none" stroke="currentColor" stroke-width="1.5"/><path d="M1 8h14M8 1c-3 4-3 10 0 14M8 1c3 4 3 10 0 14" fill="none" stroke="currentColor" stroke-width="1.2"/></svg>
      www.marlowbrookpt.example
    </div>
  </article>

  <article class="panel panel-cover" style="background:var(--white)">
    <div class="brand">
      <span class="brand-name">Marlow Brook</span>
    </div>
    <div class="photo" style="top:105px;height:500px;background:linear-gradient(160deg,#eef1f5,#cfd8e4 50%,#b7c6d8)" role="img" aria-label="Photo of a father holding his daughter while a doctor talks with them"></div>
    <svg class="curve" style="top:540px" height="320" viewBox="0 0 370 320" aria-hidden="true">
      <path d="M0 70 Q185 -10 370 20 L370 320 L0 320 Z" fill="var(--navy)"/>
      <path d="M0 56 Q185 -24 370 6" fill="none" stroke="var(--cyan)" stroke-width="6"/>
    </svg>
    <div class="cover-title">
      <h1 class="title">Pediatric<br>Pelvic Health</h1>
      <p class="subtitle">Treating infants, children<br>&amp; adolescents</p>
    </div>
    <div class="url-pill" style="bottom:36px">
      <svg width="16" height="16" viewBox="0 0 16 16" aria-hidden="true"><circle cx="8" cy="8" r="7" fill="none" stroke="currentColor" stroke-width="1.5"/><path d="M1 8h14M8 1c-3 4-3 10 0 14M8 1c3 4 3 10 0 14" fill="none" stroke="currentColor" stroke-width="1.2"/></svg>
      www.marlowbrookpt.example
    </div>
  </article>
</section>

<section class="spread spread-inside">

  <article class="panel panel-blue panel-help">
    <div class="help-copy copy">
      <h2 class="serif-head section-head">We Help</h2>
      <p>Although millions of children suffer from pelvic floor dysfunction, it often takes a long time to receive the right treatment.</p>
      <p>Typically, children are toilet trained by age 4. After age 4, bowel and bladder dysfunction is considered a major medical issue that affects the family unit.</p>
      <p>Pelvic problems in children greatly influence the quality of life, self-image, social interactions, participation in sports, etc.</p>
      <p>A pelvic physical therapist can help restore normality in bladder and bowel function and prevent the progression of problems that, if untreated, may be carried over into adult life.</p>
    </div>
    <div class="photo" style="top:600px;height:260px;background:linear-gradient(135deg,#e9e4de,#d6c3b6 50%,#c4d3e3)" role="img" aria-label="Photo of a doctor waving to a mother and her young daughter"></div>
    <svg class="curve" style="top:570px" height="70" viewBox="0 0 370 70" aria-hidden="true">
      <path d="M0 0 L370 0 L370 20 Q185 70 0 40 Z" fill="var(--navy-deep)"/>
      <path d="M370 20 Q185 70 0 40" fill="none" stroke="var(--cyan)" stroke-width="5"/>
    </svg>
  </article>

  <article class="panel panel-light panel-special" style="background:var(--white)">
    <div class="special-top copy">
      <h2 class="serif-head section-head">We Specialize</h2>
      <p>Although millions of children suffer from pelvic floor dysfunction, it often takes a long time to receive the right treatment.</p>
      <p>Typically, children are toilet trained by age 4. After age 4, bowel and bladder dysfunction is considered a major medical issue that affects the family unit.</p>
    </div>
    <div class="photo" style="top:300px;height:240px;background:linear-gradient(135deg,#f6efe9,#e8d6c8 50%,#dfe6ee)" role="img" aria-label="Photo of a smiling mother lying with her two young children"></div>
    <div class="special-bottom copy">
      <p>Pelvic problems in children greatly influence the quality of life, self-image, social interactions, participation in sports, etc.</p>
      <p>A pelvic physical therapist can help restore normality in bladder and bowel function and prevent the progression of problems that, if untreated, may be carried over into adult life.</p>
    </div>
    <div class="cta-pill">Visit our website for more information</div>
  </article>

  <article class="panel panel-blue panel-partner">
    <div class="photo" style="top:0;height:290px;background:linear-gradient(135deg,#eef2f7,#c9d6e6 55%,#8fa6c4)" role="img" aria-label="Photo of a boy asleep in bed holding a teddy bear"></div>
    <svg class="curve" style="top:240px" height="70" viewBox="0 0 370 70" aria-hidden="true">
      <path d="M0 50 Q185 0 370 20 L370 70 L0 70 Z" fill="var(--navy)"/>
      <path d="M0 50 Q185 0 370 20" fill="none" stroke="var(--cyan)" stroke-width="5"/>
    </svg>
    <div class="partner-copy copy">
      <h2 class="serif-head section-head">We Partner</h2>
      <p>Pelvic dysfunction problems in children in general, and in those with neurological pathologies even more, are markedly different from those in adults.</p>
      <p>This is a therapist who needs to work with parents, teachers, and other healthcare professionals such as urologists, GI doctors, pediatric physical therapists and psychologists to provide an integrated and comprehensive plan of care.</p>
      <p class="partner-note">Our team at Marlow Brook works closely with families and referring doctors to build a clear, caring plan.</p>
    </div>
    <div class="url-bar">
      <svg width="16" height="16" viewBox="0 0 16 16" aria-hidden="true"><circle cx="8" cy="8" r="7" fill="none" stroke="currentColor" stroke-width="1.5"/><path d="M1 8h14M8 1c-3 4-3 10 0 14M8 1c3 4 3 10 0 14" fill="none" stroke="currentColor" stroke-width="1.2"/></svg>
      www.marlowbrookpt.example
    </div>
  </article>
</section>

</body>
</html>
```